Enterprise Application UI beautification

We have an enterprise application that is being redesigned. A screenshot from the new UX/UI is provided. The current UI design is OK but we would like it to look better. The key goals of the UI are to look like a premium product (think luxury brand) and for it to be visually very appealing/attractive. When people see the UI we want them to have a significant, positive reaction. They should "ooh" and "ahh". This is a product sold to large enterprises, not consumers. The current UI is a little plain. The colors we want to use are blue, yellow, black, white and gray. We probably don't want different colors but feel free to use any variations within or close to that color scheme that you see fit. Also feel free to modify the spacing, icons, widgets, tables, fonts, etc.

Target Market(s)

Large enterprise customers (Summit 300).

Number of Pages Required

1 page

Font styles to use
Sans Serif

Colors
3277b5

Requirements
Must have
• A premium feel.

```html
<!DOCTYPE html>
<html lang="en">
<head>
<meta charset="utf-8">
<title>Data Sources</title>
<link rel="stylesheet" href="https://fonts.googleapis.com/css2?family=Poppins:wght@400;500;600;700&family=Roboto:wght@400;500&display=swap">
<style>
:root{
  --rail:#5a1fd1;
  --topbar:#240c58;
  --accent:#5b21d6;
  --pink:#d21ce0;
  --ink:#1d1d24;
  --muted:#8d8d96;
  --line:#e3e3e8;
  --page:#ececef;
  --panel:#ffffff;
  --head:#ebebee;
  --gutter:#dadadd;
  --active:#b7f0a3;
  --icon:#a9a9b1;
  --blue:#1a7fe0;
  --red:#e32b2b;
  --green:#1fbf6a;
}
*{box-sizing:border-box;margin:0;padding:0}
html,body{width:1200px;height:675px;overflow:hidden;background:var(--page)}
body{font-family:"Poppins",sans-serif;color:var(--ink)}
.app{position:relative;width:1200px;height:675px;overflow:hidden;background:var(--page)}
.abs{position:absolute}

/* rail */
.rail{left:0;top:0;width:66px;height:675px;background:var(--rail)}
.brand{position:absolute;left:0;top:14px;width:66px;text-align:center;color:#fff;font-size:11px;font-weight:600;letter-spacing:.5px}
.brand::before{content:"";display:block;width:10px;height:10px;border-radius:50%;background:#fff;margin:0 auto 3px}
.rail-item{position:absolute;left:0;width:66px;height:36px;display:flex;align-items:center;justify-content:center}
.rail-item.active{background:#fff;height:58px}
.rail-item svg{width:18px;height:18px}

/* list */
.list{left:66px;top:0;width:265px;height:675px;background:#fff}
.list h1{position:absolute;left:24px;top:36px;font-size:15px;font-weight:700}
.list .add{position:absolute;left:229px;top:41px}
.search{position:absolute;left:24px;top:69px;width:219px;height:25px;border:1px solid var(--line);border-radius:3px;font-family:"Roboto",sans-serif;font-style:italic;font-size:9px;color:#8a8a92;padding:7px 0 0 27px}
.search svg{position:absolute;left:9px;top:6px}
.src{position:absolute;left:0;width:265px;height:61px;padding:15px 0 0 25px}
.src.sel{background:#f1f1f3}
.src.sel::after{content:"";position:absolute;right:0;top:0;width:3px;height:61px;background:var(--pink)}
.src .name{font-size:11.5px;color:#2a2a30}
.src .kind{font-size:9.5px;color:var(--muted);margin-top:1px}

/* top bar */
.topbar{left:331px;top:0;width:869px;height:46px;background:var(--topbar)}
.user{position:absolute;right:28px;top:10px;display:flex;align-items:center;gap:8px;color:#fff;font-size:11px;font-weight:600}
.avatar{width:25px;height:25px;border-radius:50%;background:linear-gradient(135deg,#f3d6c4,#b98a6a)}

/* header */
.title{left:355px;top:72px;font-size:15px;font-weight:700}
.tools{left:603px;top:75px;display:flex;gap:24px}
.test{left:1057px;top:70px;width:118px;height:24px;background:#fff;border-radius:12px;box-shadow:0 2px 6px rgba(0,0,0,.12);font-size:10px;font-weight:500;color:var(--topbar);display:flex;align-items:center;justify-content:center;gap:4px}

.cell{position:absolute;height:44px;background:#fff;padding:8px 0 0 9px}
.cell .lbl{font-size:8.5px;color:#55555d}
.cell .val{font-size:10.5px;font-weight:500;color:#2a2a30;margin-top:2px}
.cell.ok{background:var(--active)}

.section{left:355px;top:238px;font-size:15px;font-weight:700}

/* objects */
.obj{position:absolute;left:357px;width:774px;background:var(--panel)}
.gut{position:absolute;left:1133px;width:38px;background:var(--gutter);display:flex;align-items:center;justify-content:center}
.toggle{width:21px;height:21px;border-radius:50%;background:#fff;display:flex;align-items:center;justify-content:center;color:var(--accent);font-size:16px;font-weight:600;line-height:1}
.obj-name{position:absolute;left:12px;font-size:12.5px;font-weight:500;color:#3a3a42}
.fields{position:absolute;right:22px;top:10px;font-size:12.5px;font-weight:500;color:#3a3a42;display:flex;align-items:center;gap:5px}
.thead{position:absolute;left:11px;top:38px;width:754px;height:39px;background:var(--head);font-size:10px;font-weight:500;color:#4a4a52}
.thead span{position:absolute;top:13px}
.row{position:absolute;left:0;width:774px;height:20px;font-family:"Roboto",sans-serif;font-size:9.5px;color:#2a2a30}
.row .c{position:absolute;top:4px}
.row svg{position:absolute;top:2px}
.chk{position:absolute;left:354px;top:3px;width:12px;height:12px;border:1px solid #8c8c94;border-radius:1px}
</style>
</head>
<body>
<div class="app">
<svg width="0" height="0" style="position:absolute">
  <defs>
    <symbol id="i-search" viewBox="0 0 16 16"><circle cx="6.5" cy="6.5" r="4.5" fill="none" stroke="currentColor" stroke-width="1.6"/><path d="M10 10l4 4" stroke="currentColor" stroke-width="1.8"/></symbol>
    <symbol id="i-doc" viewBox="0 0 16 16"><rect x="2" y="3" width="9" height="10" fill="none" stroke="currentColor" stroke-width="1.3"/><path d="M5 1h9v10" fill="none" stroke="currentColor" stroke-width="1.3"/><path d="M4 6h5M4 8h5M4 10h3" stroke="currentColor"/></symbol>
    <symbol id="i-share" viewBox="0 0 16 16"><circle cx="3" cy="8" r="2.2" fill="currentColor"/><circle cx="13" cy="3" r="2.2" fill="currentColor"/><circle cx="13" cy="13" r="2.2" fill="currentColor"/><path d="M3 8l10-5M3 8l10 5" stroke="currentColor" stroke-width="1.4"/></symbol>
    <symbol id="i-target" viewBox="0 0 16 16"><circle cx="8" cy="8" r="4.5" fill="none" stroke="currentColor" stroke-width="1.6"/><circle cx="8" cy="8" r="1.6" fill="currentColor"/><path d="M8 1v3M8 12v3M1 8h3M12 8h3" stroke="currentColor" stroke-width="1.6"/></symbol>
    <symbol id="i-play" viewBox="0 0 16 16"><path d="M4 2l10 6-10 6z" fill="currentColor"/></symbol>
    <symbol id="i-clip" viewBox="0 0 16 16"><rect x="2.5" y="2.5" width="11" height="12" rx="1" fill="none" stroke="currentColor" stroke-width="1.3"/><rect x="5.5" y="1" width="5" height="3" fill="currentColor"/><path d="M8 6.5v5M5.5 9h5" stroke="currentColor" stroke-width="1.3"/></symbol>
    <symbol id="i-card" viewBox="0 0 16 16"><rect x="1" y="3" width="14" height="10" rx="1.5" fill="none" stroke="currentColor" stroke-width="1.3"/><rect x="1" y="5.5" width="14" height="2" fill="currentColor"/></symbol>
    <symbol id="i-user" viewBox="0 0 16 16"><circle cx="8" cy="5" r="3.2" fill="currentColor"/><path d="M2.5 15c0-4 2.5-6 5.5-6s5.5 2 5.5 6z" fill="currentColor"/></symbol>
    <symbol id="i-edit" viewBox="0 0 16 16"><path d="M8 3H2v11h11V8" fill="none" stroke="currentColor" stroke-width="1.6"/><path d="M13 1.5l1.8 1.8-7 7H6V8.5z" fill="currentColor"/></symbol>
    <symbol id="i-x" viewBox="0 0 16 16"><circle cx="8" cy="8" r="7" fill="currentColor"/><path d="M5.3 5.3l5.4 5.4M10.7 5.3l-5.4 5.4" stroke="#fff" stroke-width="1.8"/></symbol>
    <symbol id="i-plus" viewBox="0 0 16 16"><circle cx="8" cy="8" r="7.5" fill="currentColor"/><path d="M8 4v8M4 8h8" stroke="#fff" stroke-width="1.8"/></symbol>
  </defs>
</svg>

<aside class="abs rail">
  <div class="brand">Lumen</div>
  <div class="rail-item" style="top:66px"><svg viewBox="0 0 20 20"><circle cx="6" cy="7" r="2.5" fill="#fff"/><circle cx="14" cy="7" r="2.5" fill="#fff"/><circle cx="10" cy="6" r="3" fill="#fff"/><path d="M2 15c0-3 2-4.5 4-4.5s4 1.5 4 4.5zM10 15c0-3 2-4.5 4-4.5s4 1.5 4 4.5z" fill="#fff"/><path d="M5 16c0-4 2.5-6 5-6s5 2 5 6z" fill="#fff"/></svg></div>
  <div class="rail-item" style="top:133px"><svg viewBox="0 0 20 20"><path d="M5 16a4 4 0 010-8 5 5 0 019.5-1A4.5 4.5 0 0115 16z" fill="#fff"/></svg></div>
  <div class="rail-item active" style="top:188px"><svg viewBox="0 0 20 20"><path d="M5 2h7l4 4v12H5z" fill="var(--accent)"/><path d="M12 2v4h4" fill="#c9b6f5"/></svg></div>
  <div class="rail-item" style="top:267px"><svg viewBox="0 0 20 20"><rect x="4" y="3" width="12" height="15" rx="1.5" fill="#fff"/><rect x="7" y="1.5" width="6" height="3" rx="1" fill="#fff" stroke="var(--rail)"/><path d="M7 11l2 2 4-4" stroke="var(--rail)" stroke-width="1.8" fill="none"/></svg></div>
  <div class="rail-item" style="top:333px"><svg viewBox="0 0 20 20"><rect x="3" y="4" width="14" height="14" rx="1.5" fill="#fff"/><path d="M6 2v4M14 2v4" stroke="#fff" stroke-width="2"/><path d="M5 9h10v7H5z" fill="var(--rail)"/><path d="M6 10h2v2H6zM9 10h2v2H9zM12 10h2v2h-2zM6 13h2v2H6zM9 13h2v2H9zM12 13h2v2h-2z" fill="#fff"/></svg></div>
  <div class="rail-item" style="top:394px"><svg viewBox="0 0 20 20"><circle cx="10" cy="10" r="7.5" fill="#fff"/><path d="M12.8 8a3.2 3.2 0 100 4" stroke="var(--rail)" stroke-width="2" fill="none"/></svg></div>
</aside>

<section class="abs list">
  <h1>Data Sources</h1>
  <svg class="add" width="13" height="13" style="color:var(--accent)"><use href="#i-plus"/></svg>
  <div class="search"><svg width="11" height="11" style="color:#555"><use href="#i-search"/></svg>Search</div>
  <div class="src sel" style="top:121px"><div class="name">Skyforce - Sandbox</div><div class="kind">Skyforce.io</div></div>
  <div class="src" style="top:185px"><div class="name">Polar Test 1 (administrator)</div><div class="kind">PolarSQL</div></div>
  <div class="src" style="top:249px"><div class="name">Polar Test 2 (administrator)</div><div class="kind">PolarSQL</div></div>
  <div class="src" style="top:312px"><div class="name">Sadga</div><div class="kind">Skyforce.io</div></div>
  <div class="src" style="top:375px"><div class="name">Skyforce Test 1 (masterd ev)</div><div class="kind">PolarSQL</div></div>
  <div class="src" style="top:438px"><div class="name">SKFC - Field Entry</div><div class="kind">Skyforce.io</div></div>
  <div class="src" style="top:502px"><div class="name">SKFC 44</div><div class="kind">Skyforce.io</div></div>
  <div class="src" style="top:565px"><div class="name">SKFC 66</div><div class="kind">Skyforce.io</div></div>
</section>

<header class="abs topbar">
  <div class="user">
    <svg width="14" height="14" viewBox="0 0 20 20"><circle cx="10" cy="10" r="6" fill="none" stroke="#fff" stroke-width="4" stroke-dasharray="3 2.3"/><circle cx="10" cy="10" r="4.5" fill="#fff"/><circle cx="10" cy="10" r="2" fill="var(--topbar)"/></svg>
    <span>Dana Reyes</span>
    <div class="avatar" role="img" aria-label="User profile photo"></div>
    <svg width="9" height="6" viewBox="0 0 10 6"><path d="M1 1l4 4 4-4" stroke="#fff" stroke-width="1.4" fill="none"/></svg>
  </div>
</header>

<h2 class="abs title">Skyforce - Sandbox</h2>
<div class="abs tools">
  <svg width="15" height="15" style="color:var(--accent)"><use href="#i-edit"/></svg>
  <svg width="15" height="15" viewBox="0 0 16 16"><rect x="4" y="1" width="11" height="11" rx="1.5" fill="var(--accent)"/><path d="M2 4v10h10" stroke="var(--accent)" stroke-width="1.6" fill="none"/></svg>
  <svg width="15" height="15" viewBox="0 0 16 16"><path d="M2 3h12v1.5H2zM6 1.5h4V3H6zM3.5 5h9l-.8 10H4.3z" fill="var(--accent)"/></svg>
</div>
<div class="abs test"><svg width="9" height="11" viewBox="0 0 10 14"><path d="M6 0L1 8h3.5L3 14l6-9H5.5z" fill="var(--accent)"/></svg>Test Connection</div>

<div class="cell" style="left:355px;top:112px;width:154px"><div class="lbl">Data Source Name</div><div class="val">Skyforce - Sandbox</div></div>
<div class="cell ok" style="left:513px;top:112px;width:154px"><div class="lbl">Status</div><div class="val">Active</div></div>
<div class="cell" style="left:671px;top:112px;width:188px"><div class="lbl">Last Updated by</div><div class="val">harlow.test</div></div>
<div class="cell" style="left:863px;top:112px;width:154px"><div class="lbl">Security Token</div><div class="val">tadkaji4234ifndkn3</div></div>
<div class="cell" style="left:1021px;top:112px;width:154px"><div class="lbl">Connected App</div><div class="val">No</div></div>
<div class="cell" style="left:355px;top:161px;width:154px"><div class="lbl">Data Source Type</div><div class="val">Application</div></div>
<div class="cell" style="left:513px;top:161px;width:154px"><div class="lbl">Created By</div><div class="val">harlow.test</div></div>
<div class="cell" style="left:671px;top:161px;width:188px"><div class="lbl">Username</div><div class="val">masterdev@dev.northdata.net</div></div>
<div class="cell" style="left:863px;top:161px;width:154px"><div class="lbl">Environment Type</div><div class="val">Production</div></div>
<div class="cell" style="left:1021px;top:161px;width:154px"></div>

<h2 class="abs section">Data Objects</h2>

<div class="obj" style="top:284px;height:233px">
  <div class="obj-name" style="top:11px">Account</div>
  <div class="fields">Fields <svg width="13" height="13" style="color:var(--accent)"><use href="#i-plus"/></svg></div>
  <div class="thead">
    <span style="left:12px">Field Name ↓</span>
    <span style="left:158px">Data Type ↓</span>
    <span style="left:321px">Primary Key</span>
    <span style="left:436px">Rule Types</span>
    <span style="left:606px">Sensitive Data</span>
    <span style="left:705px">Actions</span>
  </div>

  <div class="row" style="top:90px">
    <span class="c" style="left:22px">Account Description</span><span class="c" style="left:170px">Common.Text</span>
    <div class="chk" style="display:flex;align-items:center;justify-content:center"><svg width="9" height="9" viewBox="0 0 10 10"><path d="M2 5l2 2 4-5" stroke="#333" stroke-width="1.3" fill="none"/></svg></div>
    <span class="c" style="left:444px;top:-2px;font-size:17px;color:#222;font-family:Poppins,sans-serif">a</span>
    <svg width="12" height="12" style="left:468px;color:var(--icon)"><use href="#i-search"/></svg>
    <svg width="12" height="12" style="left:492px;color:#333"><use href="#i-doc"/></svg>
    <svg width="12" height="12" style="left:516px;color:var(--icon)"><use href="#i-share"/></svg>
    <svg width="12" height="12" style="left:541px;color:var(--icon)"><use href="#i-target"/></svg>
    <svg width="11" height="11" style="left:566px;color:var(--icon)"><use href="#i-play"/></svg>
    <svg width="12" height="12" style="left:623px;color:var(--icon)"><use href="#i-clip"/></svg>
    <svg width="14" height="12" style="left:648px;color:var(--icon)"><use href="#i-card"/></svg>
    <svg width="12" height="12" style="left:675px;color:var(--icon)"><use href="#i-user"/></svg>
    <svg width="13" height="13" style="left:717px;color:var(--blue)"><use href="#i-edit"/></svg>
    <svg width="12" height="12" style="left:740px;color:var(--red)"><use href="#i-x"/></svg>
  </div>

  <div class="row" style="top:124px">
    <span class="c" style="left:22px">Account Fax</span><span class="c" style="left:170px">Address. Address Line 3</span>
    <div class="chk"></div>
    <span class="c" style="left:444px;top:-2px;font-size:17px;color:var(--icon);font-family:Poppins,sans-serif">a</span>
    <svg width="12" height="12" style="left:468px;color:var(--icon)"><use href="#i-search"/></svg>
    <svg width="12" height="12" style="left:492px;color:#333"><use href="#i-doc"/></svg>
    <svg width="12" height="12" style="left:516px;color:var(--icon)"><use href="#i-share"/></svg>
    <svg width="12" height="12" style="left:541px;color:var(--icon)"><use href="#i-target"/></svg>
    <svg width="11" height="11" style="left:566px;color:var(--icon)"><use href="#i-play"/></svg>
    <svg width="12" height="12" style="left:623px;color:var(--icon)"><use href="#i-clip"/></svg>
    <svg width="14" height="12" style="left:648px;color:var(--icon)"><use href="#i-card"/></svg>
    <svg width="12" height="12" style="left:675px;color:var(--icon)"><use href="#i-user"/></svg>
    <svg width="13" height="13" style="left:717px;color:var(--blue)"><use href="#i-edit"/></svg>
    <svg width="12" height="12" style="left:740px;color:var(--red)"><use href="#i-x"/></svg>
  </div>

  <div class="row" style="top:159px">
    <span class="c" style="left:22px">Account ID</span><span class="c" style="left:170px">Common ID</span>
    <div class="chk"></div>
    <span class="c" style="left:444px;top:-2px;font-size:17px;color:#b21ed8;font-family:Poppins,sans-serif">a</span>
    <svg width="12" height="12" style="left:468px;color:var(--green)"><use href="#i-search"/></svg>
    <svg width="12" height="12" style="left:492px;color:var(--icon)"><use href="#i-doc"/></svg>
    <svg width="12" height="12" style="left:516px;color:var(--icon)"><use href="#i-share"/></svg>
    <svg width="12" height="12" style="left:541px;color:var(--icon)"><use href="#i-target"/></svg>
    <svg width="11" height="11" style="left:566px;color:var(--icon)"><use href="#i-play"/></svg>
    <svg width="12" height="12" style="left:623px;color:var(--icon)"><use href="#i-clip"/></svg>
    <svg width="14" height="12" style="left:648px;color:var(--icon)"><use href="#i-card"/></svg>
    <svg width="12" height="12" style="left:675px;color:var(--icon)"><use href="#i-user"/></svg>
    <svg width="13" height="13" style="left:717px;color:var(--blue)"><use href="#i-edit"/></svg>
    <svg width="12" height="12" style="left:740px;color:var(--red)"><use href="#i-x"/></svg>
  </div>

  <div class="row" style="top:194px">
    <span class="c" style="left:22px">Account Name</span><span class="c" style="left:170px">Address. Address Line 2</span>
    <div class="chk"></div>
    <span class="c" style="left:444px;top:-2px;font-size:17px;color:var(--icon);font-family:Poppins,sans-serif">a</span>
    <svg width="12" height="12" style="left:468px;color:var(--icon)"><use href="#i-search"/></svg>
    <svg width="12" height="12" style="left:492px;color:#333"><use href="#i-doc"/></svg>
    <svg width="12" height="12" style="left:516px;color:var(--icon)"><use href="#i-share"/></svg>
    <svg width="12" height="12" style="left:541px;color:var(--icon)"><use href="#i-target"/></svg>
    <svg width="11" height="11" style="left:566px;color:var(--icon)"><use href="#i-play"/></svg>
    <svg width="12" height="12" style="left:623px;color:var(--icon)"><use href="#i-clip"/></svg>
    <svg width="14" height="12" style="left:648px;color:var(--icon)"><use href="#i-card"/></svg>
    <svg width="12" height="12" style="left:675px;color:var(--icon)"><use href="#i-user"/></svg>
    <svg width="13" height="13" style="left:717px;color:var(--blue)"><use href="#i-edit"/></svg>
    <svg width="12" height="12" style="left:740px;color:var(--red)"><use href="#i-x"/></svg>
  </div>
</div>
<div class="gut" style="top:284px;height:233px"><div class="toggle">−</div></div>

<div class="obj" style="top:524px;height:36px"><div class="obj-name" style="top:8px">Asset</div></div>
<div class="gut" style="top:524px;height:36px"><div class="toggle">+</div></div>
<div class="obj" style="top:565px;height:36px"><div class="obj-name" style="top:8px">Asset Token Event</div></div>
<div class="gut" style="top:565px;height:36px"><div class="toggle">+</div></div>
<div class="obj" style="top:606px;height:36px"><div class="obj-name" style="top:8px">Asset Relationship</div></div>
<div class="gut" style="top:606px;height:36px"><div class="toggle">+</div></div>
</div>
</body>
</html>
```